Flooring Billboard Highlighting Large In Stock Inventory

Looking to create a billboard that primarily highlights our logo but also calls out our large in stock inventory and has the city we are located in and phone number at the bottom. Looking for a professional looking design, that is simplistic yet informative.

Location: Maple Falls, WI, Near Exit 114

Phone: (715) 381-6094

Website: www.plankhavenstore.example

Products: Carpet, Hardwood, Laminate, Vinyl, Luxury Vinyl Plank & Window Treatments

Callouts:
-Free Estimates
-Wisconsin's In Stock Flooring Store
-Slogan: "Big city selection, small town service"

Target Market(s)

Home buyers, DIY'ers, Remoderls, designers

Industry/Entity Type

Flooring, Construction

Font styles to use
Serif

Requirements
Must have
• My logo, location, phone number and call out our large in stock inventory
Nice to have
• Call out the products we have and our slogan

```html
<!DOCTYPE html>
<html lang="en">
<head>
<meta charset="utf-8">
<title>Plank Haven Billboard</title>
<link href="https://fonts.googleapis.com/css2?family=Montserrat:wght@700;800&family=Lato:wght@400;700&display=swap" rel="stylesheet">
<style>
  :root {
    --rust: #b9612a;
    --teal: #0f8a91;
    --white: #ffffff;
  }
  * { margin: 0; padding: 0; box-sizing: border-box; }
  html, body { width: 1200px; height: 1200px; overflow: hidden; background: var(--white); }
  .canvas { position: relative; width: 1200px; height: 1200px; }
  .billboard { position: absolute; width: 874px; height: 398px; background: var(--white); }
  .billboard--rust { left: 164px; top: 144px; box-shadow: 3px 4px 6px rgba(0,0,0,0.35); --main: var(--rust); --band: var(--teal); }
  .billboard--teal { left: 172px; top: 618px; --main: var(--teal); --band: var(--rust); }
  .shapes { position: absolute; inset: 0; width: 874px; height: 398px; }
  .brand { position: absolute; left: 52px; top: 40px; display: flex; align-items: center; gap: 12px; }
  .brand__mark { width: 44px; height: 44px; background: var(--teal); }
  .brand__name { font-family: "Montserrat", sans-serif; font-weight: 800; font-size: 34px; color: var(--rust); line-height: 1; }
  .headline, .estimates, .phone {
    position: absolute; font-family: "Montserrat", sans-serif; font-weight: 800;
    color: var(--white); white-space: nowrap;
  }
  .headline { left: 392px; top: 7px; font-size: 42px; line-height: 54px; }
  .estimates { left: 528px; top: 146px; font-size: 41px; line-height: 41px; }
  .slogan {
    position: absolute; left: 584px; top: 192px; font-family: "Lato", sans-serif; font-weight: 400;
    font-size: 32px; line-height: 39px; color: var(--white); white-space: nowrap;
  }
  .phone { left: 606px; top: 286px; font-size: 31px; line-height: 32px; font-weight: 700; }
  .location {
    position: absolute; left: 2px; right: 0; top: 342px; height: 56px;
    display: flex; align-items: center; justify-content: center; white-space: nowrap;
    font-family: "Lato", sans-serif; font-weight: 700; font-size: 37px; color: var(--white);
  }
</style>
</head>
<body>
<div class="canvas">
  <section class="billboard billboard--rust">
    <svg class="shapes" viewBox="0 0 874 398">
      <defs>
        <linearGradient id="floorA" x1="0" y1="0" x2="1" y2="0">
          <stop offset="0" stop-color="#a59d94"/><stop offset="0.28" stop-color="#9c9288"/>
          <stop offset="0.4" stop-color="#8f6d52"/><stop offset="0.62" stop-color="#ad8a6c"/>
          <stop offset="0.72" stop-color="#c9c9c9"/><stop offset="1" stop-color="#dcdcdc"/>
        </linearGradient>
      </defs>
      <polygon points="328,0 874,0 874,342 592,342 476,134 386,134" fill="var(--main)"/>
      <polygon role="img" aria-label="Room interior showing carpet, hardwood and stone tile flooring" points="2,152 456,152 572,342 2,342" fill="url(#floorA)"/>
      <rect x="2" y="342" width="872" height="56" fill="var(--band)"/>
    </svg>
    <div class="brand"><span class="brand__mark"></span><span class="brand__name">Plank Haven</span></div>
    <h1 class="headline">Wisconsin's In Stock<br>Flooring store</h1>
    <p class="estimates">Free Estimates</p>
    <p class="slogan">Big city selection,<br>small town service</p>
    <p class="phone">(715) 381-6094</p>
    <p class="location">Location :&nbsp; Maple Falls, WI, Near Exit 114</p>
  </section>

  <section class="billboard billboard--teal">
    <svg class="shapes" viewBox="0 0 874 398">
      <defs>
        <linearGradient id="floorB" x1="0" y1="0" x2="1" y2="0">
          <stop offset="0" stop-color="#a59d94"/><stop offset="0.28" stop-color="#9c9288"/>
          <stop offset="0.4" stop-color="#8f6d52"/><stop offset="0.62" stop-color="#ad8a6c"/>
          <stop offset="0.72" stop-color="#c9c9c9"/><stop offset="1" stop-color="#dcdcdc"/>
        </linearGradient>
      </defs>
      <polygon points="328,0 874,0 874,342 592,342 476,134 386,134" fill="var(--main)"/>
      <polygon role="img" aria-label="Room interior showing carpet, hardwood and stone tile flooring" points="2,152 456,152 572,342 2,342" fill="url(#floorB)"/>
      <rect x="0" y="342" width="874" height="56" fill="var(--band)"/>
    </svg>
    <div class="brand"><span class="brand__mark"></span><span class="brand__name">Plank Haven</span></div>
    <h1 class="headline">Wisconsin's In Stock<br>Flooring store</h1>
    <p class="estimates">Free Estimates</p>
    <p class="slogan">Big city selection,<br>small town service</p>
    <p class="phone">(715) 381-6094</p>
    <p class="location">Location :&nbsp; Maple Falls, WI, Near Exit 114</p>
  </section>
</div>
</body>
</html>
```